We need to design Labels of one of Our Brand QuelaVant Lotion.

The purpose of this product is to keep mosquitoes away.
There are 3 variants of this lotion. So we need 3 designs for the product. These variants details are mentioned below:

1) Mosquito Repellent Lotion with Lavender Fragrance.
2) Mosquito Repellent Lotion with Natural Ingredients.
3) Mosquito Repellent Lotion for kids.

Kindly note the bottle will be WHITE for all the variants. Cap will of the bottle will be with accordance to the color of label. In the picture it is red just for presentation.

Kindly share design of Repellent Lotion with Lavendar Fragrance initially and if we give your positive feedback, then you may add further variants of the design.

The bottle shape is attached along with keylines. Also attaching logo. If there is any other option for logo, you can suggest which we would probably keep our existing logo.

Target Market(s)

B+, B, C+

Industry/Entity Type

Product

Colors
a54499
6b449b

Requirements
Must have
• Mosquito
• 100ml
Nice to have
• Purple color as background
Should not have
• Lavendar flower

```html
<!DOCTYPE html>
<html lang="en">
<head>
<meta charset="utf-8">
<title>QuelaVant Mosquito Repellent Lotion – Lavender Label</title>
<link rel="stylesheet" href="https://fonts.googleapis.com/css2?family=Montserrat:wght@600;700;800&family=Lato:wght@400;700&display=swap">
<style>
  :root {
    --page-bg: #ffffff;
    --label-white: #ffffff;
    --label-edge: #e6e1ea;
    --band-light: #45a9ec;
    --band-dark: #2a6cc2;
    --brand-blue: #2b63b8;
    --title-plum: #6b1f7a;
    --plum-soft: #7a3b8c;
    --purple-a: #a54499;
    --purple-b: #6b449b;
    --text-white: #ffffff;
    --stop-red: #d8202a;
    --insect-dark: #222222;
  }
  * { margin: 0; padding: 0; box-sizing: border-box; }
  html, body {
    width: 1200px; height: 1000px; overflow: hidden;
    background: var(--page-bg);
  }
  .canvas { position: relative; width: 1200px; height: 1000px; }
  .label {
    position: absolute; left: 340px; top: 120px;
    width: 520px; height: 760px;
  }
  .label-shape { position: absolute; inset: 0; }
  .label-text { position: absolute; font-family: "Montserrat", sans-serif; }

  .band-text {
    font-family: "Montserrat", sans-serif;
    font-weight: 600; font-size: 24px; letter-spacing: 1px;
    fill: var(--text-white);
  }
  .new-tag {
    left: 64px; top: 190px;
    font-weight: 700; font-size: 18px; color: var(--brand-blue);
    letter-spacing: 1px;
  }
  .brand-name {
    left: 60px; top: 214px;
    font-weight: 800; font-size: 60px; line-height: 1;
    color: var(--brand-blue); letter-spacing: 1px;
  }
  .product-title { left: 64px; top: 408px; color: var(--title-plum); }
  .product-title .main {
    display: block; font-weight: 800; font-size: 50px; line-height: 1;
  }
  .product-title .sub {
    display: block; font-weight: 700; font-size: 24px; line-height: 1.2;
    padding-bottom: 8px; border-bottom: 2px solid var(--plum-soft);
    width: 384px;
  }
  .product-title .variant {
    display: block; font-family: "Lato", sans-serif; font-weight: 400;
    font-size: 20px; margin-top: 8px; color: var(--title-plum);
  }
  .claims {
    left: 64px; top: 590px;
    font-family: "Lato", sans-serif; font-size: 22px; line-height: 1.25;
    color: var(--text-white);
  }
  .mosquito-icon {
    position: absolute; left: 392px; top: 582px;
    width: 66px; height: 66px;
  }
  .warning {
    left: 64px; top: 676px;
    font-family: "Lato", sans-serif; font-weight: 700; font-size: 13px;
    color: var(--text-white); letter-spacing: 0.3px;
    border: 1.5px solid var(--text-white); padding: 4px 8px;
  }
  .volume {
    left: 0; width: 520px; top: 712px; text-align: center;
    font-family: "Lato", sans-serif; font-size: 26px; color: var(--text-white);
  }
</style>
</head>
<body>
<main class="canvas">
  <section class="label" aria-label="Lotion label, lavender variant">
    <svg class="label-shape" viewBox="0 0 520 760" width="520" height="760" aria-hidden="true">
      <defs>
        <linearGradient id="bandGradient" x1="0" y1="0" x2="1" y2="0">
          <stop offset="0" stop-color="var(--band-light)"/>
          <stop offset="1" stop-color="var(--band-dark)"/>
        </linearGradient>
        <linearGradient id="purpleFade" x1="0" y1="0" x2="0" y2="1">
          <stop offset="0" stop-color="#ffffff"/>
          <stop offset="0.35" stop-color="#e6c9e4"/>
          <stop offset="0.7" stop-color="var(--purple-a)"/>
          <stop offset="1" stop-color="var(--purple-b)"/>
        </linearGradient>
        <clipPath id="labelClip">
          <rect x="0" y="0" width="520" height="760" rx="28"/>
        </clipPath>
        <path id="bandLineOne" d="M34 95 Q260 26 520 70"/>
        <path id="bandLineTwo" d="M38 123 Q262 54 520 98"/>
      </defs>
      <g clip-path="url(#labelClip)">
        <rect class="label-base" x="0" y="0" width="520" height="760" fill="var(--label-white)"/>
        <rect class="label-fade" x="0" y="330" width="520" height="430" fill="url(#purpleFade)"/>
        <path class="label-band" d="M0 70 Q250 0 520 40 L520 118 Q260 80 0 156 Z" fill="url(#bandGradient)"/>
        <text class="band-text"><textPath href="#bandLineOne">DERMATOLOGICALLY</textPath></text>
        <text class="band-text"><textPath href="#bandLineTwo">TESTED</textPath></text>
      </g>
      <rect x="1" y="1" width="518" height="758" rx="28" fill="none" stroke="var(--label-edge)" stroke-width="2"/>
    </svg>

    <p class="label-text new-tag">NEW</p>
    <p class="label-text brand-name">QUELAVANT</p>

    <h1 class="label-text product-title">
      <span class="main">MOSQUITO</span>
      <span class="sub">REPELLENT LOTION</span>
      <span class="variant">with Lavender Fragrance</span>
    </h1>

    <p class="label-text claims">Anti-Dengue<br>Hypoallergenic</p>
    <svg class="mosquito-icon" viewBox="0 0 66 66" role="img" aria-label="No-mosquito symbol: crossed-out mosquito">
      <circle cx="33" cy="33" r="31" fill="#ffffff"/>
      <g class="mosquito" stroke="var(--insect-dark)" stroke-linecap="round" fill="none">
        <ellipse cx="24" cy="24" rx="9" ry="4" transform="rotate(-35 24 24)" fill="#cfd6dc" stroke-width="1"/>
        <ellipse cx="40" cy="22" rx="9" ry="4" transform="rotate(30 40 22)" fill="#cfd6dc" stroke-width="1"/>
        <line x1="25" y1="42" x2="42" y2="25" stroke-width="4"/>
        <circle cx="44" cy="23" r="3" fill="var(--insect-dark)" stroke="none"/>
        <line x1="46" y1="21" x2="54" y2="13" stroke-width="1.2"/>
        <path d="M31 36 L22 30 L14 34" stroke-width="1.2"/>
        <path d="M33 34 L28 44 L20 50" stroke-width="1.2"/>
        <path d="M36 31 L40 42 L38 52" stroke-width="1.2"/>
        <path d="M38 29 L46 36 L52 46" stroke-width="1.2"/>
      </g>
      <circle cx="33" cy="33" r="27" fill="none" stroke="var(--stop-red)" stroke-width="5"/>
      <line x1="14" y1="14" x2="52" y2="52" stroke="var(--stop-red)" stroke-width="5"/>
    </svg>

    <p class="label-text warning">KEEP OUT OF REACH OF CHILDREN &amp; PETS</p>
    <p class="label-text volume">100mL</p>
  </section>
</main>
</body>
</html>
```